Bottle labels and logo for small distillery

Harbor Stillhouse is a small beginning project of handcrafted distillery producing cider spirit (same as apple wine spirit) and apple vodka from apple wine. There are not many similar small distilleries in the Baltic Sea region and very few of them produce apple brandy, so the concept and the product itself are unique. That is the reason we are not developing any distinctive brand and we are sticking to two elements – company name ‘Harbor Stillhouse OÜ’ and product name ‘Orchardine’. Best branding solution for us would be to have a clear logo instead of words.

In the future it is most likely that the product range will broaden by some type of sweet liqueurs like apple-liqueur and black-currant-liqueur and both will be mixtures of natural juice and apple brandy.

We have tested the product itself and more or less chosen proper bottle and closing. Example of the shape of the bottle:

https://www.vessel-depot.example.co.uk/Glass-vessels/Glass-vessels/500ml-glass-vessels/500ml-clear-glass-vessel-Rondel.html

Sizes of bottles:
500 ml Height (without cap) 350 mm, external diameter 60 mm;
375 ml Height (without cap) 330 mm, external diameeter 55 mm;

The bottle cap/closing is going to be waxed, and should look something like that:

http://img.picstash-example.com/qR7Tz.jpg

The design has two separate parts: (1) paper bottle label and (2) print on the bottle.

Front side – printed to the bottle, preferably a symbol without text, for better quality of print rather a vector graphics (monochrome or up to 3-single colour picture). We would like to use the symbol also as an enterprise logo if possible (but logo and bottle print can also be different if designer decides so). It should give a hint to apple based distillate (but, we do not want to narrow down creators fantasy so if you have a good idea please don’t hold back). Just to offer a dumb examples:
https://moodbinder-example.com/entry/51839206
https://www.pinboardly-example.ca/pin/719302846615902418/?lp=true https://www.stockframe-example.com/image-vector/decorative-apple-flora-ornaments-leaf-flower-482017356?src=QXP_tbRkLw8YpH3JcV_29m-2-50
NB! these are just examples of style, contents are more or less random.

Back side – a rectangular shaped label glued to the bottle. Label should not be a square but rather oblong and narrow. The colour of the label shouldn’t be white but rather light yellow, light brown or light creamy. Some examples:

https://www.pinboardly-example.co.uk/pin/830174529266108354 https://www.pinboardly-example.co.uk/pin/591840372605183924

Label has to contain such information:
1) (Product in large print) Orchardine
2) (product) apple wine spirit
3) (Neto amount) 50 cl; / 35 cl
4) (Ethanol in large print) 45%; / 55%
5) (Producer) Produced by Harbor Stillhouse, Lõunamaa 48213, Rannaküla, Sõstra 7;
6) (raw material and technology) Made in Estonia. Product is made of Estonian apple wine and distilled in reflux still in small batches
7) (distillate) Distillate 85%
8) (batch no) Batch no: (stamp) …
9) (note) produced with utmost pleasure
10) (note) Consume responsibly
11) (signature) distiller: …

We also need the label to be designed in Estonian as follows:
1) Orchardine
2) Õunaveini destillaat
3) 50 cl; / 35 cl
4) 45% / 55%
5) Toodetud Harbor Stillhouse OÜ poolt, Lõunamaal 48213, Rannaküla, Sõstra 7;
6) Toodetud Eestis, eestimaisest õunaveinist ja destilleeritud käsitööna väikeste partiidena
7) Destillaat 85%
8) Partii nr:
9) Toodetud puhtast rõõmust
10) Tarbige vastutustundlikult!
11) Meister:

Design as such can be the same. Since we are planning to bottle the product in 375 ml and 500 ml bottles and dilute it down to 45% and 55%. So, there should be 37,5 cl 45%, 50 cl 45%; 37,5 cl 55%; 50 cl 55%.

We assume that in case of 37,5 cl and 50 cl bottles we can use the same design and just resize the printed image and paper-label a bit.

Since the product is handmade and high quality we would like to stress credibility. Not as important as the first purchase is the second purchase of clients – the label should not be shocking but rather trustworthy. And classy in the very best sense.

We are hoping to have a long term business relationship with possible future designer.

Target Market(s)

Adult male alcohol consumers

Industry/Entity Type

Food Production

Logo Text

Harbor Stillhouse

Colors

Designer to choose colors to be used in the design.

```html
<!DOCTYPE html>
<html lang="en">
<head>
<meta charset="utf-8">
<title>Harbor Stillhouse OÜ – Orchardine labels</title>
<link href="https://fonts.googleapis.com/css2?family=Oswald:wght@400;500&family=Rye&family=Oleo+Script&family=Homemade+Apple&display=swap" rel="stylesheet">
<style>
  :root {
    --bg-top: #f4f4f4;
    --bg-bottom: #dcdcdc;
    --ink: #1e1e1e;
    --ink-soft: #555049;
    --label-cream: #f3ead2;
    --label-edge: #e4d7b6;
    --accent-red: #8b1a12;
    --olive: #5b5a32;
    --sign-blue: #2b4fb0;
    --sketch: #d8ccaf;
    --glass-deep: #4a0704;
    --glass-mid: #8e1408;
    --glass-light: #b3260f;
    --print-white: #f7f3ea;
  }
  * { margin: 0; padding: 0; box-sizing: border-box; }
  html, body { width: 1200px; height: 1200px; overflow: hidden; }
  body {
    background: radial-gradient(ellipse at 50% 30%, var(--bg-top) 0%, #ececec 55%, var(--bg-bottom) 100%);
    position: relative;
    font-family: "Oswald", sans-serif;
    color: var(--ink);
  }

  /* Company mark */
  .brand-mark {
    position: absolute;
    left: 60px; top: 170px;
    width: 360px;
    display: flex; flex-direction: column; align-items: center; gap: 18px;
  }
  .brand-mark__square { width: 44px; height: 44px; background: var(--ink); }
  .brand-mark__name {
    font-weight: 500; font-size: 28px; letter-spacing: 0.5px;
    text-transform: uppercase; color: var(--ink); white-space: nowrap;
  }

  /* Print on the glass */
  .glass-print {
    position: absolute;
    left: 470px; top: 80px;
    width: 290px; height: 1040px;
    border-radius: 60px 60px 36px 36px;
    background: linear-gradient(90deg, var(--glass-deep) 0%, var(--glass-mid) 22%, var(--glass-light) 50%, var(--glass-mid) 78%, var(--glass-deep) 100%);
    display: flex; flex-direction: column; align-items: center; justify-content: center; gap: 16px;
    padding-top: 160px;
  }
  .glass-print__square { width: 30px; height: 30px; background: var(--print-white); }
  .glass-print__name {
    font-weight: 500; font-size: 22px; letter-spacing: 0.4px;
    text-transform: uppercase; color: var(--print-white); white-space: nowrap;
  }

  /* Back label (drawn at base size, scaled per placement) */
  .back-label {
    position: absolute;
    width: 276px; height: 481px;
    background: var(--label-cream);
    border: 1px solid var(--label-edge);
    border-radius: 138px;
    box-shadow: 0 10px 26px rgba(0,0,0,0.08);
    text-align: center;
    transform-origin: top left;
  }
  .back-label--sheet { left: 60px; top: 470px; transform: scale(1.3); }
  .back-label--applied { left: 830px; top: 410px; transform: scale(1.18); }

  .back-label__brand {
    position: absolute; top: 108px; left: 0; right: 0;
    display: flex; flex-direction: column; align-items: center; gap: 6px;
  }
  .back-label__brand-square { width: 14px; height: 14px; background: var(--ink); }
  .back-label__brand-name {
    font-size: 10px; font-weight: 500; text-transform: uppercase; color: var(--ink);
  }
  .back-label__title {
    position: absolute; top: 210px; left: 0; right: 0;
    font-family: "Rye", serif; font-size: 24px; font-weight: 400; letter-spacing: 0.5px;
    text-transform: uppercase; color: var(--ink);
  }
  .back-label__subtitle {
    position: absolute; top: 243px; left: 0; right: 0;
    font-family: "Oleo Script", cursive; font-size: 10px; color: var(--accent-red);
  }
  .back-label__illustration {
    position: absolute; left: 96px; top: 268px; width: 84px; height: 96px;
  }
  .back-label__story {
    position: absolute; left: 98px; top: 305px; width: 80px;
    font-size: 6.6px; line-height: 1.35; color: var(--ink-soft);
  }
  .back-label__volume, .back-label__strength {
    position: absolute; top: 306px;
    font-size: 16px; font-weight: 400; color: var(--olive);
  }
  .back-label__volume { left: 52px; }
  .back-label__strength { left: 196px; }
  .back-label__note {
    position: absolute; top: 330px;
    font-family: "Oleo Script", cursive; font-size: 7px; color: var(--accent-red); white-space: nowrap;
  }
  .back-label__note--left { left: 36px; }
  .back-label__note--right { left: 190px; }
  .back-label__divider { position: absolute; top: 300px; width: 6px; height: 64px; }
  .back-label__divider--left { left: 88px; }
  .back-label__divider--right { left: 182px; }
  .back-label__batch {
    position: absolute; top: 384px; left: 0; right: 0;
    display: flex; justify-content: center; gap: 14px;
    font-family: "Oleo Script", cursive; font-size: 7px; color: var(--accent-red);
  }
  .back-label__field { display: inline-flex; align-items: flex-end; gap: 3px; }
  .back-label__field-value {
    font-family: "Homemade Apple", cursive; font-size: 5.5px; color: var(--sign-blue);
    border-bottom: 1px dotted var(--sign-blue); padding: 0 2px; line-height: 1.4;
  }
  .back-label__producer {
    position: absolute; top: 406px; left: 0; right: 0;
    font-size: 8.6px; line-height: 1.32; color: var(--olive);
  }
  .back-label__producer strong { font-weight: 500; text-transform: uppercase; }
</style>
</head>
<body>

  <section class="brand-mark" aria-label="Company logo">
    <span class="brand-mark__square"></span>
    <span class="brand-mark__name">Harbor Stillhouse OÜ</span>
  </section>

  <section class="glass-print" aria-label="Front print on the bottle glass">
    <span class="glass-print__square"></span>
    <span class="glass-print__name">Harbor Stillhouse OÜ</span>
  </section>

  <article class="back-label back-label--sheet" aria-label="Orchardine back label">
    <div class="back-label__brand">
      <span class="back-label__brand-square"></span>
      <span class="back-label__brand-name">Harbor Stillhouse OÜ</span>
    </div>
    <h1 class="back-label__title">Orchardine</h1>
    <p class="back-label__subtitle">Apple wine spirit</p>
    <svg class="back-label__illustration" viewBox="0 0 84 96" role="img" aria-label="Faint engraved apple with leaf">
      <ellipse cx="42" cy="52" rx="40" ry="40" fill="var(--sketch)" opacity="0.45"/>
    </svg>
    <p class="back-label__story">Made in Estonia.<br>Product is made of<br>Estonian apple wine<br>and distilled in reflux<br>still in small batches.</p>
    <span class="back-label__volume">50 cl</span>
    <span class="back-label__note back-label__note--left">Distillate 85%</span>
    <svg class="back-label__divider back-label__divider--left" viewBox="0 0 6 64" aria-hidden="true">
      <line x1="3" y1="0" x2="3" y2="64" stroke="var(--olive)" stroke-width="0.8"/>
    </svg>
    <span class="back-label__strength">55%</span>
    <span class="back-label__note back-label__note--right">Consume responsibly</span>
    <svg class="back-label__divider back-label__divider--right" viewBox="0 0 6 64" aria-hidden="true">
      <line x1="3" y1="0" x2="3" y2="64" stroke="var(--olive)" stroke-width="0.8"/>
    </svg>
    <div class="back-label__batch">
      <span class="back-label__field">Batch: <span class="back-label__field-value">25-08-18</span></span>
      <span class="back-label__field">Distiller: <span class="back-label__field-value">Signature Here</span></span>
    </div>
    <p class="back-label__producer">
      Produced by<br>
      <strong>Harbor Stillhouse,</strong><br>
      Lõunamaa 48213,<br>
      Rannaküla, Sõstra 7
    </p>
  </article>

  <article class="back-label back-label--applied" aria-label="Orchardine back label as applied to the bottle">
    <div class="back-label__brand">
      <span class="back-label__brand-square"></span>
      <span class="back-label__brand-name">Harbor Stillhouse OÜ</span>
    </div>
    <h2 class="back-label__title">Orchardine</h2>
    <p class="back-label__subtitle">Apple wine spirit</p>
    <svg class="back-label__illustration" viewBox="0 0 84 96" role="img" aria-label="Faint engraved apple with leaf">
      <ellipse cx="42" cy="52" rx="40" ry="40" fill="var(--sketch)" opacity="0.45"/>
    </svg>
    <p class="back-label__story">Made in Estonia.<br>Product is made of<br>Estonian apple wine<br>and distilled in reflux<br>still in small batches.</p>
    <span class="back-label__volume">50 cl</span>
    <span class="back-label__note back-label__note--left">Distillate 85%</span>
    <svg class="back-label__divider back-label__divider--left" viewBox="0 0 6 64" aria-hidden="true">
      <line x1="3" y1="0" x2="3" y2="64" stroke="var(--olive)" stroke-width="0.8"/>
    </svg>
    <span class="back-label__strength">55%</span>
    <span class="back-label__note back-label__note--right">Consume responsibly</span>
    <svg class="back-label__divider back-label__divider--right" viewBox="0 0 6 64" aria-hidden="true">
      <line x1="3" y1="0" x2="3" y2="64" stroke="var(--olive)" stroke-width="0.8"/>
    </svg>
    <div class="back-label__batch">
      <span class="back-label__field">Batch: <span class="back-label__field-value">25-08-18</span></span>
      <span class="back-label__field">Distiller: <span class="back-label__field-value">Signature Here</span></span>
    </div>
    <p class="back-label__producer">
      Produced by<br>
      <strong>Harbor Stillhouse,</strong><br>
      Lõunamaa 48213,<br>
      Rannaküla, Sõstra 7
    </p>
  </article>

</body>
</html>
```